Lumora Business Card Design

hello,
we are looking for a business card design for our Fintech Company. We are credit card processing company that is also expanding in to the crypto market. We will be focusing on crypto processing, with a crypto wallet and crypto exchange. We like the purple in the logo. We want something modern and sophisticated but at the same time simple and trust worthy to work with banks.

Industry/Entity Type

Fintech

Logo Text

Lumora

```html
<!DOCTYPE html>
<html lang="en">
<head>
<meta charset="utf-8">
<title>Lumora Business Card Set</title>
<link rel="stylesheet" href="https://fonts.googleapis.com/css2?family=Roboto:wght@400;500;700&display=swap">
<style>
  :root {
    --stage: #2e2e30;
    --paper: #ffffff;
    --purple: #3d1fa8;
    --navy: #1f2a4b;
    --lavender: rgba(200, 196, 225, 0.55);
    --ink-light: #ffffff;
    --card-w: 515px;
    --card-h: 297px;
  }
  * { box-sizing: border-box; margin: 0; padding: 0; }
  html, body { width: 1200px; height: 900px; overflow: hidden; }
  body {
    background: var(--stage);
    font-family: "Roboto", Arial, sans-serif;
    position: relative;
  }
  .card {
    position: absolute;
    width: var(--card-w);
    height: var(--card-h);
    overflow: hidden;
    background: var(--paper);
    box-shadow: 0 4px 10px rgba(0,0,0,0.45);
  }
  .card--front-pattern { left: 72px; top: 138px; }
  .card--back-strip    { left: 615px; top: 138px; }
  .card--front-large   { left: 72px; top: 464px; }
  .card--back-navy     { left: 615px; top: 464px; background: var(--navy); }

  .pattern { position: absolute; }
  .pattern--light {
    left: 0; top: 0; width: 100%; height: 100%;
    background: radial-gradient(ellipse at 35% 40%, rgba(205,202,228,0.45), rgba(255,255,255,0) 70%);
  }
  .pattern--on-purple {
    left: 0; top: 0; width: 100%; height: 100%;
    background: radial-gradient(ellipse at 60% 40%, rgba(255,255,255,0.09), rgba(255,255,255,0) 70%);
  }
  .pattern--on-navy {
    left: 0; top: 0; width: 100%; height: 72%;
    background: radial-gradient(ellipse at 65% 45%, rgba(255,255,255,0.08), rgba(255,255,255,0) 70%);
  }

  .wordmark {
    font-family: "Roboto", Arial, sans-serif;
    font-weight: 500;
    color: var(--navy);
    letter-spacing: -2px;
    line-height: 1;
    white-space: nowrap;
  }
  .card--front-pattern .wordmark {
    position: absolute; right: 26px; bottom: 24px; font-size: 56px;
  }

  /* back with vertical wordmark */
  .strip {
    position: absolute; left: 0; top: 0; width: 145px; height: 100%;
    background: var(--paper);
  }
  .strip .wordmark {
    position: absolute; left: 72px; top: 148px;
    font-size: 74px; color: var(--purple);
    transform: translate(-50%, -50%) rotate(-90deg);
  }
  .info-panel {
    position: absolute; left: 145px; top: 0; right: 0; height: 226px;
    background: var(--purple);
  }
  .pointer {
    position: absolute; left: 145px; top: 54px;
    width: 0; height: 0;
    border-top: 7px solid transparent; border-bottom: 7px solid transparent;
    border-left: 10px solid var(--paper);
  }
  .address-band {
    position: absolute; left: 145px; top: 226px; right: 0; bottom: 0;
    background: var(--navy);
  }
  .person { position: absolute; color: var(--ink-light); }
  .person__name { font-size: 15.5px; font-weight: 500; }
  .person__role { font-size: 11.5px; margin-top: 3px; }
  .card--back-strip .person { left: 194px; top: 51px; }
  .rule {
    position: absolute; left: 194px; top: 114px; width: 42px; height: 2px;
    background: var(--ink-light);
  }
  .contacts { position: absolute; list-style: none; color: var(--ink-light); font-size: 11.5px; }
  .contacts li { height: 17px; display: flex; align-items: center; gap: 7px; }
  .contacts svg { width: 11px; height: 11px; fill: var(--ink-light); flex: none; }
  .card--back-strip .contacts { left: 194px; top: 146px; }
  .address { position: absolute; color: var(--ink-light); font-size: 11.5px; line-height: 17px; }
  .card--back-strip .address { left: 194px; top: 246px; }

  /* front with large wordmark */
  .large-mark { position: absolute; left: 0; top: 0; width: 100%; height: 100%; }
  .large-mark text {
    font-family: "Roboto", Arial, sans-serif; font-weight: 500;
    fill: var(--navy); letter-spacing: -4px;
  }

  /* navy back */
  .card--back-navy .person { left: 42px; top: 45px; text-transform: uppercase; }
  .card--back-navy .contacts { left: 42px; top: 149px; }
  .card--back-navy .contacts li { height: 16.5px; }
  .base-band {
    position: absolute; left: 0; top: 212px; right: 0; bottom: 0;
    background: var(--purple);
  }
  .card--back-navy .address { left: 42px; top: 220px; line-height: 16.5px; }
  .logo-box {
    position: absolute; left: 264px; top: 195px; width: 251px; height: 84px;
    background: var(--paper);
    display: flex; align-items: center; justify-content: center;
  }
  .logo-box .wordmark { font-size: 50px; }
</style>
</head>
<body>

  <section class="card card--front-pattern">
    <div class="pattern pattern--light" role="img" aria-label="Faint scattered square pattern"></div>
    <div class="wordmark">Lumora</div>
  </section>

  <section class="card card--back-strip">
    <div class="strip"><div class="wordmark">Lumora</div></div>
    <div class="info-panel">
      <div class="pattern pattern--on-purple" role="img" aria-label="Faint scattered square pattern"></div>
    </div>
    <div class="pointer"></div>
    <div class="person">
      <div class="person__name">Daniel Corvell</div>
      <div class="person__role">Managing Director</div>
    </div>
    <div class="rule"></div>
    <ul class="contacts">
      <li><svg viewBox="0 0 12 12"><path d="M1 5c3-3 7-3 10 0l-2 2-1.5-1.3V4.2a6 6 0 0 0-3 0v1.5L3 7z"/></svg>555 310 42 17</li>
      <li><svg viewBox="0 0 12 12"><path d="M3.5 0.5h5a1 1 0 0 1 1 1v9a1 1 0 0 1-1 1h-5a1 1 0 0 1-1-1v-9a1 1 0 0 1 1-1zM4 2v7h4V2zM6 9.6a0.6 0.6 0 1 0 0.01 0z"/></svg>888 604 29 73</li>
      <li><svg viewBox="0 0 12 12"><path d="M1 2.5h10v7H1zM1.6 3.2 6 6.6l4.4-3.4z" fill-rule="evenodd"/></svg>d.corvell@lumora.com</li>
      <li><svg viewBox="0 0 12 12"><path d="M6 1a5 5 0 1 0 0.01 0zM6 2c.7.8 1.1 2 1.2 3.5H4.8C4.9 4 5.3 2.8 6 2zM2.1 6.5h1.7c.1 1.4.5 2.6 1.1 3.4A4 4 0 0 1 2.1 6.5zM2.1 5.5A4 4 0 0 1 4.9 2.1c-.6.8-1 2-1.1 3.4zM4.8 6.5h2.4C7.1 8 6.7 9.2 6 10c-.7-.8-1.1-2-1.2-3.5zM7.1 2.1a4 4 0 0 1 2.8 3.4H8.2c-.1-1.4-.5-2.6-1.1-3.4zM8.2 6.5h1.7a4 4 0 0 1-2.8 3.4c.6-.8 1-2 1.1-3.4z"/></svg>www.lumora.com</li>
    </ul>
    <div class="address-band"></div>
    <div class="address">48 Harbor Lane<br>Brookfield, New York 10231</div>
  </section>

  <section class="card card--front-large">
    <svg class="large-mark" viewBox="0 0 515 297" aria-label="Lumora">
      <text x="18" y="302" font-size="142">Lumora</text>
    </svg>
  </section>

  <section class="card card--back-navy">
    <div class="pattern pattern--on-navy" role="img" aria-label="Faint scattered square pattern"></div>
    <div class="person">
      <div class="person__name">Daniel Corvell</div>
      <div class="person__role">Managing Director</div>
    </div>
    <ul class="contacts">
      <li>555 310 42 17</li>
      <li>888 604 29 73</li>
      <li>d.corvell@lumora.com</li>
    </ul>
    <div class="base-band"></div>
    <div class="address">48 Harbor Lane<br>Brookfield, New York 10231<br>www.lumora.com</div>
    <div class="logo-box"><div class="wordmark">Lumora</div></div>
  </section>

</body>
</html>
```